New Business Card Design Project

Need a design that will create an impact / strong impression towards our clients for our business. We are in the lighting business and we do lighting retrofits for large commercial to industrial clientele.

Target Market(s)

Lighting Industry

Industry/Entity Type

Business

Other font styles liked:
• we would like to use the font on our logo, not sure what it is though..

Requirements
Must have
• Our logo.
Nice to have
• We are open to suggestions that have to do with lighting.

```html
<!DOCTYPE html>
<html lang="en">
<head>
<meta charset="utf-8">
<title>Lumenbridge Retrofit Co. – Business Card</title>
<link href="https://fonts.googleapis.com/css2?family=Lato:wght@400;700;900&display=swap" rel="stylesheet">
<style>
  :root {
    --bg: #4a4a4c;
    --forest: #153f12;
    --leaf: #0a8036;
    --lime: #5cc45a;
    --paper: #ffffff;
    --ink: #1c1c1c;
  }
  * { box-sizing: border-box; margin: 0; padding: 0; }
  html, body { width: 1200px; height: 900px; overflow: hidden; }
  body {
    background: var(--bg);
    font-family: "Lato", sans-serif;
    position: relative;
  }
  .card {
    position: absolute;
    left: 267px;
    width: 665px;
    height: 380px;
    overflow: hidden;
    box-shadow: 0 6px 18px rgba(0,0,0,.35);
  }
  /* back */
  .card-back { top: 45px; background: var(--forest); }
  .back-brand {
    position: absolute; top: 120px; left: 0; right: 0;
    display: flex; align-items: center; justify-content: center; gap: 14px;
    color: var(--paper); font-weight: 900; font-size: 46px; letter-spacing: 1px;
  }
  .brand-mark { width: 26px; height: 26px; background: var(--lime); }
  .back-tagline {
    position: absolute; top: 186px; left: 0; right: 0; text-align: center;
    color: var(--paper); font-weight: 700; font-size: 14px; letter-spacing: 3px;
  }
  .back-web {
    position: absolute; bottom: 62px; left: 0; right: 0; text-align: center;
    color: var(--paper); font-size: 17px; letter-spacing: 1px;
  }
  /* front */
  .card-front { top: 475px; background: var(--paper); }
  .front-shapes { position: absolute; inset: 0; }
  .front-brand {
    position: absolute; top: 58px; left: 40px;
    display: flex; align-items: center; gap: 12px;
    color: var(--forest); font-weight: 900; font-size: 38px; letter-spacing: 1px;
  }
  .front-tagline {
    position: absolute; top: 112px; left: 42px;
    color: var(--forest); font-weight: 700; font-size: 11px; letter-spacing: 2.4px;
    border-top: 2px solid var(--leaf); padding-top: 5px;
  }
  .person { position: absolute; top: 180px; left: 40px; }
  .person-name { color: var(--leaf); font-weight: 700; font-size: 27px; }
  .person-role { color: var(--ink); font-size: 18px; margin-top: 2px; }
  .address {
    position: absolute; top: 282px; left: 40px;
    color: var(--ink); font-size: 19px; line-height: 1.25;
  }
  .contacts {
    position: absolute; top: 262px; left: 388px;
    list-style: none; color: var(--ink); font-size: 18px; line-height: 1.2;
  }
  .contacts li { display: flex; align-items: center; gap: 12px; margin-bottom: 2px; }
  .contacts svg { width: 16px; height: 16px; fill: var(--leaf); flex: none; }
</style>
</head>
<body>

<section class="card card-back">
  <div class="back-brand"><span class="brand-mark"></span>Lumenbridge</div>
  <p class="back-tagline">RETROFIT CO.</p>
  <p class="back-web">www.lumenbridge-co.com</p>
</section>

<section class="card card-front">
  <svg class="front-shapes" viewBox="0 0 665 380" preserveAspectRatio="none">
    <path d="M250 0 Q560 55 665 330 L665 0 Z" fill="var(--leaf)"/>
    <path d="M262 0 Q556 58 660 300 L665 300 L665 0 Z" fill="var(--paper)"/>
    <path d="M270 0 Q565 62 665 298 L665 0 Z" fill="var(--leaf)"/>
    <path d="M330 0 Q590 70 665 262 L665 0 Z" fill="var(--forest)"/>
  </svg>

  <div class="front-brand"><span class="brand-mark"></span>Lumenbridge</div>
  <p class="front-tagline">RETROFIT CO.</p>

  <div class="person">
    <p class="person-name">Mark Ellison</p>
    <p class="person-role">Manager</p>
  </div>

  <address class="address" style="font-style:normal">
    4182 North Alder Avenue<br>Elmwood, IL 60582
  </address>

  <ul class="contacts">
    <li><svg viewBox="0 0 16 16"><path d="M3 1l3 3-1.5 2c1 2 3 4 5 5l2-1.5 3 3-2 2C7 14 2 9 1 3z"/></svg>(555) 014-2700</li>
    <li><svg viewBox="0 0 16 16"><path d="M4 1h8v4H4zM1 6h14v6h-3v3H4v-3H1zM5 10v4h6v-4z"/></svg>(555) 014-2701</li>
    <li><svg viewBox="0 0 16 16"><path d="M1 3h14v10H1zM2 4l6 5 6-5v-.5H2z" fill-rule="evenodd"/></svg>info@lumenbridge-co.com</li>
    <li><svg viewBox="0 0 16 16"><circle cx="8" cy="8" r="7" fill="none" stroke="var(--leaf)" stroke-width="1.6"/><path d="M1 8h14M8 1v14" stroke="var(--leaf)" stroke-width="1.3"/><ellipse cx="8" cy="8" rx="3" ry="7" fill="none" stroke="var(--leaf)" stroke-width="1.3"/></svg>www.lumenbridge-co.com</li>
  </ul>
</section>

</body>
</html>
```